Book cover design for a collection of poetry - The Lanternfield

Book cover and back design need to be moody, nostalgic, reflective, ethereal. Melancholy and other worldly. Cover design should not be time specific to a period or place but if applicable should reflect British landscape. Book cover should be in tones of blue and must include the title and author (THE LANTERNFIELD BY DORIAN WELKBRIDGE). We love the idea of rain, and looking out of a window. See attached designs. A world you are observing but not in.

Industry/Entity Type

Book Publisher

Font styles to use
Serif
Script

Colors
3176b5
3377b5
85acd3
eaf1f7
0792cd
33a6d7
86cae7
ecf7fb
86cfc6

Requirements
Must have
• The colour blue in it, must be melancholy and reflective.
Nice to have
• Rain in the cover.
Should not have
• Any bright colours.

```html
<!DOCTYPE html>
<html lang="en">
<head>
<meta charset="utf-8">
<title>The Lanternfield – Cover Spread</title>
<link href="https://fonts.googleapis.com/css2?family=EB+Garamond:ital,wght@0,400;1,400&family=Roboto+Condensed:wght@700&display=swap" rel="stylesheet">
<style>
  :root {
    --paper: #ffffff;
    --mist: #eaf1f7;
    --haze: #9fbccc;
    --deep: #1e3e50;
    --ink: #0f2634;
    --spine: #182a36;
    --title: #86cfc6;
    --title-soft: #8fc3c9;
    --panel: rgba(40, 52, 62, 0.62);
    --text: #f2f6f8;
    --crop: #222222;
  }
  * { margin: 0; padding: 0; box-sizing: border-box; }
  html, body { width: 1200px; height: 952px; overflow: hidden; background: var(--paper); }
  .canvas { position: relative; width: 1200px; height: 952px; }

  .crop { position: absolute; background: var(--crop); }
  .crop.v { width: 1px; height: 29px; }
  .crop.h { height: 1px; width: 29px; }

  .spread { position: absolute; left: 92px; top: 95px; width: 1004px; height: 767px; overflow: hidden; }
  .rain-window {
    position: absolute; inset: 0;
    background:
      radial-gradient(ellipse 34% 22% at 50% 78%, rgba(20,50,66,.9), transparent 70%),
      radial-gradient(ellipse 46% 30% at 22% 58%, rgba(24,58,76,.85), transparent 75%),
      radial-gradient(ellipse 46% 30% at 78% 58%, rgba(24,58,76,.85), transparent 75%),
      radial-gradient(ellipse 18% 40% at 50% 25%, rgba(18,44,60,.95), transparent 75%),
      radial-gradient(ellipse 70% 20% at 50% 96%, rgba(220,232,240,.95), transparent 80%),
      radial-gradient(ellipse 30% 26% at 8% 10%, var(--paper), transparent 80%),
      radial-gradient(ellipse 30% 26% at 92% 10%, var(--paper), transparent 80%),
      linear-gradient(180deg, var(--mist) 0%, var(--haze) 30%, var(--deep) 55%, #3f6478 80%, #cddde6 100%);
  }

  .back-panel {
    position: absolute; left: 86px; top: 134px; width: 309px; height: 514px;
    background: var(--panel);
    color: var(--text); text-align: center;
    font-family: "EB Garamond", serif; font-size: 13px; line-height: 18px;
    padding: 61px 22px 0;
  }
  .back-panel p { margin-bottom: 18px; }
  .back-panel p.tight { margin-bottom: 0; }
  .back-panel .synopsis-close { font-style: italic; margin-top: 18px; }
  .back-panel .author-name {
    font-family: "Roboto Condensed", sans-serif; font-weight: 700;
    font-size: 13px; letter-spacing: .2px; margin-top: 48px; margin-bottom: 26px;
  }
  .back-panel .publisher { font-size: 12px; }

  .spine {
    position: absolute; left: 484px; top: 0; width: 38px; height: 767px;
    background: var(--spine);
  }
  .spine-title, .spine-author {
    position: absolute; left: 50%; white-space: nowrap;
    transform-origin: 0 0; transform: rotate(90deg) translateY(-50%);
  }
  .spine-title {
    top: 131px; font-family: "EB Garamond", serif; font-size: 19px;
    color: var(--title-soft); letter-spacing: 1px;
  }
  .spine-author {
    top: 533px; font-family: "Roboto Condensed", sans-serif; font-weight: 700;
    font-size: 12px; color: #d9e4ea; letter-spacing: .3px;
  }

  .front { position: absolute; left: 522px; top: 0; width: 482px; height: 767px; }
  .front-title {
    position: absolute; left: 0; right: 0; top: 380px; text-align: center;
    font-family: "EB Garamond", serif; font-weight: 400; color: var(--title);
    font-size: 44px; line-height: 64px; letter-spacing: 1px;
    text-shadow: 0 2px 6px rgba(5,20,30,.55);
    padding-left: 40px;
  }
  .front-title .line-the { display: block; font-size: 56px; }
  .author-box {
    position: absolute; top: 530px; left: 50%; transform: translateX(-50%);
    margin-left: 20px;
    border: 1px solid var(--title);
    padding: 6px 12px 5px;
    font-family: "Roboto Condensed", sans-serif; font-weight: 700;
    font-size: 18px; color: var(--text); white-space: nowrap; letter-spacing: .2px;
  }
</style>
</head>
<body>
<div class="canvas">
  <span class="crop v" style="left:90px;top:58px"></span>
  <span class="crop h" style="left:54px;top:94px"></span>
  <span class="crop v" style="left:1096px;top:58px"></span>
  <span class="crop h" style="left:1104px;top:94px"></span>
  <span class="crop v" style="left:90px;top:864px"></span>
  <span class="crop h" style="left:54px;top:862px"></span>
  <span class="crop v" style="left:1096px;top:864px"></span>
  <span class="crop h" style="left:1104px;top:862px"></span>

  <div class="spread">
    <div class="rain-window" role="img" aria-label="Blurred, mirrored view through a rain-streaked misty window in deep blue tones"></div>

    <section class="back-panel">
      <p>The Lanternfield is a collection of Poetry.</p>
      <p class="tight">Told in two parts we first meet Charles - aged, crippled and left alone in his inherited Marsh house - reflecting on his life and his marriage to beautiful Alice, who we meet in part two.</p>
      <p class="tight">Alice is suicidal, manically depressed and struggling with life as a wife and mother. She meets, harbours and falls in love with a soldier during WWII and her world is changed forever.</p>
      <p class="synopsis-close">Moving through the 20th Century, this life and the next, The Lanternfield interweaves grief, loss, the afterlife, mental illness and ultimately the true nature of love,</p>
      <p class="author-name">DORIAN WELKBRIDGE</p>
      <p class="publisher">Publisher Information</p>
    </section>

    <div class="spine">
      <span class="spine-title">THE LANTERNFIELD</span>
      <span class="spine-author">DORIAN WELKBRIDGE</span>
    </div>

    <section class="front">
      <h1 class="front-title"><span class="line-the">THE</span>LANTERNFIELD</h1>
      <div class="author-box">DORIAN WELKBRIDGE</div>
    </section>
  </div>
</div>
</body>
</html>
```